Core Values poster for display in office

We want to create a poster that displays our core values which we can print and place in our office and potentially use on our website.

DataHaven is a Cyber Security consultancy that helps its secure its clients from Cyber Criminals.

Our core values are what we live and breath everyday. They are:
- Customer love
- High performing team
- Do the right thing
- An awesome culture
- Innovative

Here they are again with more detail after each:
- Customer love – exchange in abundance
- High performing team – do whatever it takes, no passengers
- Do the right thing – be accountable, maintain our integrity
- An awesome culture – work hard, play hard, collaborate and celebrate success
- Innovative – solving problems with new ideas

We are in the process of rolling out new branding with a load of comic book style super hero's and villains. Attached are some of those images in PDF format for some business card designs for you to review if you want to incorporate, but I will upload these images to this dropbox folder once my designer sends them to me:
https://www.filecrate.example/sh/qpwlzrtkc42hsum/KKTm7VoP2wQ8yE5nLDRxUa91b?dl=0

I stumbled across another business with the same name as us and saw their values poster, which I liked conceptually.
www.datahaven.example
I've attached the image for reference (note this is not our business or values - just saying I like the concept).

Also attached is our logo in EPS format.

We would like the image editing version of the file once complete so we can edit the file in case we change or tweak our values in the near future.

Target Market(s)

This poster is to be displayed internally and maybe on our website in the hiring section

Industry/Entity Type

Office

Colors
0792cd
ffffff
f68e4e
e667a6
fbee3e

Requirements
Must have
• Must have a vibrant, impactful poster that clearly states our core values in a way so that they are understood.
• Must be print ready in high definition (large A2 size poster).
Nice to have
• Integrate our logo

```html
<!DOCTYPE html>
<html lang="en">
<head>
<meta charset="utf-8">
<title>DataHaven – Our Core Values</title>
<link href="https://fonts.googleapis.com/css2?family=Comfortaa:wght@300;400;700&family=Fredoka:wght@600&family=Questrial&display=swap" rel="stylesheet">
<style>
  :root {
    --paper: #f4f8fc;
    --brand-blue: #0792cd;
    --band-blue: #1597d5;
    --pink: #e667a6;
    --pink-soft: #e4d3d8;
    --green: #236636;
    --green-soft: #d5e2cf;
    --orange: #f68e4e;
    --lilac-soft: #d3d6e6;
    --teal-soft: #bfe0e4;
    --navy: #04293f;
    --steel-soft: #c9d6df;
    --yellow: #fbee3e;
    --purple: #8a3b97;
    --deep-blue: #0b6a9a;
    --white: #ffffff;
    --ink: #1f2a33;
    --art-blue: #7cc3ea;
  }
  html, body {
    margin: 0;
    padding: 0;
    overflow: hidden;
    background: var(--paper);
  }
  .poster {
    display: block;
    width: 849px;
    height: 1200px;
    background: var(--paper);
  }
  .headline { font-family: "Fredoka", "Comfortaa", sans-serif; font-weight: 600; filter: drop-shadow(3px 3px 0 var(--brand-blue)); }
  .headline-our { fill: var(--purple); }
  .headline-core { fill: var(--deep-blue); }
  .headline-values { fill: var(--green); }
  .value-title { font-family: "Comfortaa", sans-serif; fill: var(--white); font-weight: 400; }
  .value-key { font-weight: 300; }
  .value-key-bold { font-weight: 700; }
  .value-detail { font-family: "Questrial", sans-serif; fill: var(--ink); font-size: 31px; }
  .art { fill: var(--art-blue); opacity: 0.5; }
  .brand-name { font-family: "Comfortaa", sans-serif; font-weight: 700; fill: var(--white); font-size: 44px; }
</style>
</head>
<body>
<svg class="poster" viewBox="0 0 849 1200" width="849" height="1200" xmlns="http://www.w3.org/2000/svg">

  <!-- Customer love -->
  <polygon class="band-soft" fill="var(--pink-soft)" points="320,36 849,36 849,240 384,288"/>
  <polygon class="band" fill="var(--pink)" points="336,0 849,0 849,184 400,228" stroke="var(--brand-blue)" stroke-width="3"/>

  <!-- High performing team -->
  <polygon class="band-soft" fill="var(--green-soft)" points="160,444 849,504 849,448 200,400"/>
  <polygon class="band" fill="var(--green)" points="264,296 849,276 849,448 200,400" stroke="var(--brand-blue)" stroke-width="3"/>

  <!-- Do the right thing -->
  <polygon class="band-soft" fill="var(--lilac-soft)" points="0,612 680,636 672,682 0,654"/>
  <polygon class="band" fill="var(--orange)" points="0,480 748,496 680,636 0,612" stroke="var(--brand-blue)" stroke-width="3"/>

  <!-- An awesome culture -->
  <polygon class="band-soft" fill="var(--teal-soft)" points="184,808 849,836 849,912 136,880"/>
  <polygon class="band" fill="var(--band-blue)" points="192,700 849,680 849,836 184,808"/>

  <!-- Innovative -->
  <polygon class="band-soft" fill="var(--steel-soft)" points="0,1032 564,1028 564,1072 0,1084"/>
  <polygon class="band" fill="var(--navy)" points="0,892 580,908 564,1028 0,1032" stroke="var(--brand-blue)" stroke-width="3"/>

  <!-- Illustration areas -->
  <rect class="art" x="328" y="64" width="168" height="160" rx="60" role="img" aria-label="Illustration of a heart"/>
  <rect class="art" x="656" y="264" width="192" height="184" rx="30" role="img" aria-label="Illustration of jigsaw puzzle pieces"/>
  <rect class="art" x="680" y="500" width="160" height="220" rx="70" role="img" aria-label="Illustration of a lightbulb with a leaf"/>
  <rect class="art" x="16" y="672" width="176" height="248" rx="40" role="img" aria-label="Illustration of a jumping figure celebrating"/>
  <rect class="art" x="448" y="896" width="192" height="240" rx="60" role="img" aria-label="Illustration of a rocket launching"/>

  <!-- Title card -->
  <polygon fill="var(--yellow)" points="0,0 308,0 268,380 0,352"/>
  <polygon fill="var(--paper)" stroke="var(--brand-blue)" stroke-width="3" points="0,0 276,0 240,336 0,312"/>
  <g transform="rotate(7 140 170)">
    <text class="headline headline-our" x="86" y="88" font-size="56">Our</text>
    <text class="headline headline-core" x="30" y="166" font-size="82">core</text>
    <text class="headline headline-values" x="18" y="232" font-size="64">values</text>
  </g>
  <polyline points="86,272 104,290 156,254" fill="none" stroke="var(--yellow)" stroke-width="7" stroke-linecap="round" stroke-linejoin="round"/>

  <!-- Value titles -->
  <text class="value-title" x="820" y="150" text-anchor="end" font-size="38">Customer <tspan class="value-key" font-size="82">love</tspan></text>
  <text class="value-title" x="824" y="384" text-anchor="end" font-size="38">High performing <tspan class="value-key-bold" font-size="88">team</tspan></text>
  <text class="value-title" x="676" y="578" text-anchor="end" font-size="38">Do the <tspan class="value-key" font-size="88">right</tspan> thing</text>
  <text class="value-title" x="814" y="776" text-anchor="end" font-size="38">An awesome <tspan class="value-key" font-size="88">culture</tspan></text>
  <text class="value-title value-key" x="110" y="988" font-size="90">Innovative</text>

  <!-- Value details -->
  <text class="value-detail" x="820" y="214" text-anchor="end" transform="rotate(-5 820 214)">exchange in abundance</text>
  <text class="value-detail" x="226" y="432" transform="rotate(5 226 432)">do whatever it takes, no passengers</text>
  <text class="value-detail" x="32" y="640" transform="rotate(2 32 640)">be accountable, maintain our integrity</text>
  <text class="value-detail" x="806" y="852" text-anchor="end" transform="rotate(2.5 806 852)">work hard, play hard,</text>
  <text class="value-detail" x="816" y="898" text-anchor="end" transform="rotate(2.5 816 898)">collaborate and celebrate success</text>
  <text class="value-detail" x="30" y="1066" transform="rotate(-2.5 30 1066)">solving problems with new ideas</text>

  <!-- Footer brand bar -->
  <rect x="0" y="1120" width="849" height="80" fill="var(--brand-blue)"/>
  <text class="brand-name" x="818" y="1176" text-anchor="end">DataHaven</text>
</svg>
</body>
</html>
```